Awesome Business Card Design needed!

Hey there.
I'm looking for a simple but awesome business card design.
Type of company: Online advertisement agency
(please don't use the typical business people or statistics images on the card)
The front has to display the business name
and possibly some sort of logo ( perhaps something with the two M's of the biz name )
And the back of the card should say:
Name
Phone
Email
Let your imagination flow.
here are some designs that I like and that you can use as inspiration.
Simple but Awesome
http://images.pixelvantor.net/designs/55128_877673_43091_thumbnail.jpg
http://images.pixelvantor.net/designs/37714_747642_40106_image.jpg
http://images.pixelvantor.net/designs/55128_877673_43091_image.jpg
http://images.pixelvantor.net/designs/51321_781878_43091_image.jpg
http://images.pixelvantor.net/designs/33378_399063_15912_image.jpg
http://images.pixelvantor.net/designs/2337_271604_9495_image.jpg
good luck

```html
<!DOCTYPE html>
<html lang="en">
<head>
<meta charset="utf-8">
<title>Velmora Media – Business Card</title>
<link rel="stylesheet" href="https://fonts.googleapis.com/css2?family=Arimo:wght@400&display=swap">
<style>
  :root {
    --page-bg: #5d5e60;
    --card-light: #bdbdbd;
    --card-mid: #a2a2a2;
    --card-dark: #878787;
    --brand-orange: #e8a232;
    --brand-yellow: #e2cc56;
    --ink: #1c1c1c;
    --rule: #111111;
    --muted-tan: #b89a62;
    --muted-olive: #b3aa74;
    --font-main: "Arimo", Arial, Helvetica, sans-serif;
  }
  * { box-sizing: border-box; margin: 0; padding: 0; }
  html, body {
    width: 924px;
    height: 1200px;
    overflow: hidden;
    background: var(--page-bg);
    font-family: var(--font-main);
  }
  .sheet {
    position: relative;
    width: 924px;
    height: 1200px;
  }
  .card {
    position: absolute;
    left: 155px;
    width: 570px;
    height: 329px;
    background: radial-gradient(ellipse at 50% 50%, var(--card-light) 0%, var(--card-mid) 55%, var(--card-dark) 100%);
  }
  .card--front { top: 131px; }
  .card--back { top: 476px; }

  .front-brand {
    position: absolute;
    left: 0;
    right: 0;
    top: 0;
    bottom: 0;
    display: flex;
    align-items: center;
    justify-content: center;
    gap: 18px;
  }
  .brand-dot {
    width: 34px;
    height: 34px;
    border-radius: 50%;
    background: var(--brand-yellow);
    flex: none;
  }
  .front-brand__name {
    font-size: 58px;
    font-weight: 400;
    color: var(--brand-orange);
    white-space: nowrap;
  }

  .back-brand {
    position: absolute;
    left: 0;
    top: 0;
    width: 222px;
    height: 329px;
    display: flex;
    align-items: center;
    justify-content: center;
  }
  .back-brand__lockup {
    display: flex;
    align-items: center;
    gap: 16px;
    transform: rotate(-90deg);
    white-space: nowrap;
  }
  .back-brand__lockup .brand-dot { width: 26px; height: 26px; }
  .back-brand__name {
    font-size: 38px;
    color: var(--brand-yellow);
  }
  .divider {
    position: absolute;
    left: 222px;
    top: 18px;
    width: 3px;
    height: 293px;
    background: var(--rule);
  }
  .contact {
    position: absolute;
    left: 247px;
    top: 74px;
    list-style: none;
    font-size: 24px;
    color: var(--ink);
  }
  .contact li { height: 65px; }

  .mark-preview {
    position: absolute;
    left: 15px;
    top: 1040px;
    display: flex;
    align-items: center;
    gap: 16px;
  }
  .mark-preview .brand-dot { background: var(--muted-olive); width: 40px; height: 40px; }
  .mark-preview__name {
    font-size: 62px;
    color: var(--muted-tan);
    white-space: nowrap;
  }
</style>
</head>
<body>
  <main class="sheet">
    <section class="card card--front" aria-label="Card front">
      <div class="front-brand">
        <span class="brand-dot"></span>
        <span class="front-brand__name">Velmora Media</span>
      </div>
    </section>

    <section class="card card--back" aria-label="Card back">
      <div class="back-brand">
        <div class="back-brand__lockup">
          <span class="brand-dot"></span>
          <span class="back-brand__name">Velmora Media</span>
        </div>
      </div>
      <div class="divider"></div>
      <ul class="contact">
        <li>Name</li>
        <li>Phone</li>
        <li>email</li>
      </ul>
    </section>

    <div class="mark-preview">
      <span class="brand-dot"></span>
      <span class="mark-preview__name">Velmora Media</span>
    </div>
  </main>
</body>
</html>
```